Tavrin Telecom Corporate Website & Social Branding

We are looking for a new website for our startup telecom which provides UCaaS, SD-WAN, Business SMS/MMS, Video Conferencing, Managed Network Service & more.

Target Market(s)

Small offices from 1-250 users

Industry/Entity Type

Telecomunications

Coding

Coded - Design and coding required

Colors
0054AA
0677BA
7BADD7
CADEEF
E8F1F8

```html
<!DOCTYPE html>
<html lang="en">
<head>
<meta charset="utf-8">
<title>Tavrin Telecom</title>
<link href="https://fonts.googleapis.com/css2?family=Montserrat:wght@400;500;600;700&display=swap" rel="stylesheet">
<style>
:root{
  --ink:#231f20;
  --dark:#252122;
  --accent:#1e9ad6;
  --btn:#0c8fd2;
  --sky:#8fd6f7;
  --muted:#555;
  --soft:#f4f4f4;
  --navy:#0054aa;
}
*{margin:0;padding:0;box-sizing:border-box}
html,body{width:1200px;height:4574px;overflow:hidden;background:#fff}
body{position:relative;font-family:'Montserrat',sans-serif;color:var(--ink)}
.abs{position:absolute}
.brand{font-weight:700;font-size:30px;color:var(--navy);display:flex;align-items:center;gap:10px}
.brand i{display:block;width:26px;height:26px;border-radius:50%;background:var(--navy)}
.top-contact{font-size:13px;color:var(--ink)}
.btn{display:flex;align-items:center;justify-content:center;font-weight:600;font-size:15px;color:#fff;background:var(--btn)}
.btn-outline{display:flex;align-items:center;justify-content:center;font-weight:600;font-size:15px;color:var(--accent);border:2px solid var(--ink);background:#fff}
.hero-title{font-weight:700;font-size:52px;line-height:1;letter-spacing:.5px}
.blue{color:var(--accent)}
.para{font-size:14px;line-height:1.6;color:var(--muted)}
.nav a{position:absolute;font-weight:700;font-size:16px;color:var(--ink);text-decoration:none;transform:translateX(-50%)}
.photo{background:linear-gradient(135deg,#8c8577,#c9b59c 45%,#6b5e51)}
.sec-title{font-weight:700;font-size:36px;text-align:center;width:1200px;left:0}
.feature h4{font-size:16px;font-weight:600;margin-bottom:8px}
.feature p{font-size:12.5px;line-height:1.6;color:#777;width:370px}
.feature svg{position:absolute;left:-42px;top:-4px}
.svc{position:absolute;width:370px;border-top:1px solid #3d393a;padding-top:20px;color:#fff}
.svc h4{font-size:16px;font-weight:600;display:flex;align-items:center;gap:10px}
.svc p{font-size:12.5px;color:#ccc;margin-top:14px}
.svc .arr{position:absolute;right:0;top:22px}
.svc.active{background:var(--btn);width:423px;padding:20px 22px;border:none}
.svc.active p{color:#fff}
.svc.active .arr{right:24px}
.card{position:absolute;background:var(--soft);border-radius:8px;overflow:hidden}
.card .img{height:149px;background:linear-gradient(135deg,#6d7a86,#c8cdd2 55%,#8b9096)}
.card h5{font-size:16px;font-weight:700;padding:14px 18px 0;line-height:1.35}
.card a{display:inline-block;margin:10px 18px;font-size:14px;font-weight:600;color:var(--accent);border-bottom:2px solid var(--accent);padding-bottom:4px}
.big-title{font-weight:700;font-size:36px;line-height:46px}
.partner{position:absolute;top:3864px;font-weight:700;font-size:22px;color:#3b3b3b;transform:translateX(-50%)}
.cta{background:linear-gradient(90deg,#1c2e66,#2d52a8 70%,#3566c4)}
.foot h6{font-size:14px;font-weight:700;margin-bottom:14px}
.foot li{list-style:none;font-size:13px;color:#555;height:28px;display:flex;align-items:center;gap:10px}
.foot li i{display:block;width:20px;height:20px;border-radius:50%;background:var(--btn)}
</style>
</head>
<body>

<!-- header -->
<div class="abs brand" style="left:140px;top:22px"><i></i>Tavrin Telecom</div>
<div class="abs top-contact" style="left:584px;top:38px">&#9742; Get in touch: (208) 555-0147</div>
<div class="abs top-contact" style="left:822px;top:38px">&#128274; Login</div>
<div class="abs btn" style="left:914px;top:25px;width:146px;height:42px">Get Started</div>

<h1 class="abs hero-title" style="left:140px;top:112px">A BETTER ASSISTANT</h1>
<div class="abs hero-title blue" style="right:140px;top:168px">FOR YOUR SMALL BUSINESS</div>
<p class="abs para" style="left:140px;top:246px;width:560px">Lorem ipsum dolor sit amet, consectetur adipiscing elit aucibus enim. Tristique imperdiet metus, risus nunc quis.</p>

<nav class="nav">
  <a style="left:320px;top:322px">COMPANY</a>
  <a style="left:511px;top:322px">SOLUTIONS</a>
  <a style="left:706px;top:322px">PRODUCTS</a>
  <a style="left:888px;top:322px">PRICING</a>
</nav>

<div class="abs photo" role="img" aria-label="Businessman working at a laptop while holding a phone in an office" style="left:0;top:373px;width:1200px;height:689px"></div>

<!-- communication solution -->
<h2 class="abs sec-title" style="top:1175px">COMMUNICATION <span class="blue">SOLUTION</span></h2>
<p class="abs" style="left:250px;top:1234px;width:700px;text-align:center;font-weight:600;font-size:16px;line-height:1.5">Lorem ipsum dolor sit amet, enim ornare scelerisque nibh purus.consectetur adipiscing elit. Faucibus enim ornare.</p>
<div class="abs" style="left:534px;top:1298px;width:132px;height:3px;background:var(--accent)"></div>

<p class="abs para" style="left:139px;top:1347px;width:440px;font-size:14.5px;color:#333">Diam quis viverra tincidunt velit eu felis hendrerit in convallis. Blandit velit lorem integer consectetur. Pretium donec malesuada quis ac ultricies ac.</p>

<div class="abs feature" style="left:187px;top:1478px">
  <svg width="24" height="24" viewBox="0 0 24 24" fill="none" stroke="#1e9ad6" stroke-width="1.6"><rect x="3" y="4" width="18" height="13" rx="1"/><path d="M7 8h2M11 8h2M15 8h2M7 12h2M11 12h2M15 12h2M9 20h6"/></svg>
  <h4>Powerful, easy to use software</h4>
  <p>Lorem ipsum dolor sit amet, consectetur adipiscing elit aucibus enim.</p>
</div>
<div class="abs feature" style="left:187px;top:1570px">
  <svg width="24" height="24" viewBox="0 0 24 24" fill="none" stroke="#1e9ad6" stroke-width="1.6"><circle cx="11" cy="11" r="7"/><path d="M16 16l5 5M8 11h6"/></svg>
  <h4>No contracts. No hidden fees</h4>
  <p>Lorem ipsum dolor sit amet, consectetur adipiscing elit aucibus enim. Tristique imperdiet metus, risus nunc quis.</p>
</div>
<div class="abs feature" style="left:187px;top:1662px">
  <svg width="24" height="24" viewBox="0 0 24 24" fill="none" stroke="#1e9ad6" stroke-width="1.6"><circle cx="12" cy="12" r="9"/><circle cx="12" cy="12" r="3"/></svg>
  <h4>Awesome customer service</h4>
  <p>Lorem ipsum dolor sit amet, consectetur adipiscing elit aucibus enim risus nunc .</p>
</div>

<div class="abs" role="img" aria-label="Laptop showing a video call beside a hand holding a phone" style="left:628px;top:1349px;width:572px;height:391px;background:linear-gradient(135deg,#5d6b4c,#c9ced3 45%,#8c8f94)"></div>

<!-- services -->
<svg class="abs" style="left:0;top:1780px" width="1200" height="860" viewBox="0 0 1200 860">
  <path d="M0 12 C300 90 700 140 1200 60 L1200 120 L0 120 Z" fill="var(--sky)"/>
  <path d="M0 62 C350 150 800 160 1200 65 L1200 800 L0 770 Z" fill="var(--dark)"/>
  <path d="M0 770 C400 830 850 870 1200 775 L1200 840 C850 900 400 850 0 770 Z" fill="var(--sky)"/>
  <path d="M0 770 C400 820 850 840 1200 775 L1200 760 L0 760 Z" fill="var(--dark)"/>
</svg>
<h2 class="abs sec-title" style="top:2014px;color:#fff">POWERFUL <span class="blue">SERVICES</span></h2>

<div class="svc" style="left:193px;top:2125px"><h4>UCaaS</h4><p>Lorem ipsum dolor sit amet, consectetur adipiscing elit</p><span class="arr">&#10230;</span></div>
<div class="svc" style="left:637px;top:2125px"><h4>SD-WAN</h4><p>Lorem ipsum dolor sit amet, consectetur adipiscing elit</p><span class="arr">&#10230;</span></div>
<div class="svc" style="left:193px;top:2224px"><h4>Business SMS/MMS</h4><p>Lorem ipsum dolor sit amet, consectetur adipiscing elit</p><span class="arr">&#10230;</span></div>
<div class="svc active" style="left:612px;top:2222px"><h4>Video Conferencing</h4><p>Lorem ipsum dolor sit amet, consectetur adipiscing elit</p><span class="arr">&#10230;</span></div>
<div class="svc" style="left:193px;top:2323px"><h4>Managed Network Service</h4><p>Lorem ipsum dolor sit amet, consectetur adipiscing elit</p><span class="arr">&#10230;</span></div>
<div class="svc" style="left:637px;top:2322px"><h4>Business SMS/MMS</h4><p>Lorem ipsum dolor sit amet, consectetur adipiscing elit</p><span class="arr">&#10230;</span></div>

<div class="abs btn" style="left:527px;top:2487px;width:144px;height:43px">All Services</div>

<!-- case studies -->
<div class="card" style="left:-96px;top:2730px;width:211px;height:280px"><div class="img" role="img" aria-label="Laptop on a desk"></div><h5>Blandit velit lorem integer consectetur</h5><a>View Case Studies</a></div>
<div class="card" style="left:140px;top:2730px;width:211px;height:280px"><div class="img" role="img" aria-label="Laptop on a desk"></div><h5>Blandit velit lorem integer consectetur</h5><a>View Case Studies</a></div>
<div class="card" style="left:376px;top:2730px;width:211px;height:280px"><div class="img" role="img" aria-label="Laptop on a desk"></div><h5>Blandit velit lorem integer consectetur</h5><a>View Case Studies</a></div>
<div class="abs" style="left:567px;top:2855px;width:42px;height:42px;border-radius:50%;background:#fff;box-shadow:0 2px 8px rgba(0,0,0,.15);display:flex;align-items:center;justify-content:center;color:var(--accent);font-size:18px">&#8594;</div>

<h2 class="abs big-title" style="left:653px;top:2743px">TRANSFORMING<br><span class="blue">COMPANIES</span> AROUND<br>THE WORLD</h2>
<p class="abs para" style="left:653px;top:2900px;width:420px;color:#444">Diam quis viverra tincidunt velit eu felis hendrerit in convallis. Blandit velit lorem integer consectetur. Pretium donec malesuada quis ac ultricies ac. Lorem ipsum dolor sit amet, consectetur adipiscing</p>
<div class="abs btn-outline" style="left:653px;top:3023px;width:211px;height:43px;border-color:#444">See All Case Studies</div>

<!-- assistant -->
<div class="abs" style="left:650px;top:3185px;font-weight:700;font-size:120px;color:#f3f3f3;letter-spacing:-2px">Tavrin</div>
<h2 class="abs big-title" style="left:140px;top:3228px"><span>YOUR </span><span class="blue">HELPFUL</span><br>ASSISTANT</h2>
<p class="abs para" style="left:140px;top:3344px;width:420px;font-size:13px;color:#333">Diam quis viverra tincidunt velit eu felis hendrerit in convallis. Blandit velit lorem integer consectetur.</p>

<svg class="abs" style="left:140px;top:3418px" width="34" height="28" viewBox="0 0 34 28" fill="none" stroke="#1e9ad6" stroke-width="1.6"><rect x="2" y="3" width="30" height="20" rx="1"/><rect x="8" y="9" width="9" height="7"/></svg>
<svg class="abs" style="left:353px;top:3418px" width="30" height="30" viewBox="0 0 30 30" fill="none" stroke="#1e9ad6" stroke-width="1.6"><rect x="3" y="3" width="24" height="24"/><rect x="10" y="10" width="6" height="6"/><rect x="16" y="14" width="6" height="6"/></svg>
<div class="abs" style="left:140px;top:3455px;font-size:13px;font-weight:600">Tools For Every One</div>
<div class="abs" style="left:353px;top:3455px;font-size:13px;font-weight:600">Prebuilt Integrations</div>
<p class="abs" style="left:140px;top:3488px;width:170px;font-size:13px;line-height:1.55;color:#333">Diam quis viverra tincidunt velit eu felis hendrerit in convallis.</p>
<p class="abs" style="left:353px;top:3488px;width:170px;font-size:13px;line-height:1.55;color:#333">Diam quis viverra tincidunt velit eu felis hendrerit in convallis.</p>
<div class="abs btn-outline" style="left:140px;top:3582px;width:169px;height:43px">Find Out More</div>

<div class="abs" role="img" aria-label="Support agent wearing a headset pointing at charts on a monitor" style="left:575px;top:3320px;width:625px;height:313px;background:linear-gradient(100deg,#fff 0%,#5e7187 18%,#b9c6d6 55%,#e8eef4 100%)"></div>

<!-- partners -->
<h2 class="abs sec-title" style="top:3778px">CRM &amp; HELPDESK</h2>
<div class="partner" style="left:178px">Cloudvane</div>
<div class="partner" style="left:305px">Hubwell</div>
<div class="partner" style="left:458px">Zentra</div>
<div class="partner" style="left:613px">Chatterly</div>
<div class="partner" style="left:752px">Deskly</div>
<div class="partner" style="left:902px">Flowline</div>
<div class="partner" style="left:1037px">Talkbay</div>

<!-- cta -->
<div class="abs cta" style="left:0;top:3971px;width:1200px;height:293px"></div>
<h2 class="abs" style="left:0;top:4024px;width:1200px;text-align:center;color:#fff;font-weight:700;font-size:30px;line-height:37px">READY TO EXPLORE? SIGNUP &amp; GET 70%<br>DISCOUNT FOR THE FIRST MONTH</h2>
<p class="abs" style="left:0;top:4104px;width:1200px;text-align:center;color:#fff;font-size:13px;line-height:1.5">Lorem ipsum dolor sit amet, consectetur adipiscing elit aucibus enim.<br>Tristique imperdiet metus, risus nunc quis.</p>
<div class="abs" style="left:334px;top:4166px;width:367px;height:43px;background:#fff;display:flex;align-items:center;padding-left:30px;font-size:13px;color:#777">Email address</div>
<div class="abs btn" style="left:710px;top:4166px;width:153px;height:43px;border:2px solid #fff;background:var(--btn)">Try for FREE</div>

<!-- footer -->
<div class="abs brand" style="left:140px;top:4340px;font-size:24px"><i style="width:22px;height:22px"></i>Tavrin Telecom</div>
<p class="abs" style="left:140px;top:4400px;width:240px;font-size:13px;line-height:1.5;color:#555">Lorem ipsum dolor sit amet, consectetur adipiscing elit aucibus enim. Tristique imperdiet metus, risus nunc quis.</p>
<div class="abs foot" style="left:536px;top:4334px"><h6>QUICK LINKS</h6><ul><li>Solutions</li><li>Products</li><li>Pricing</li><li>Login</li></ul></div>
<div class="abs foot" style="left:742px;top:4334px"><h6>SERVICES</h6><ul><li>UCaaS</li><li>SD-WAN</li><li>Business SMS/MMS</li><li>Video Conferencing</li></ul></div>
<div class="abs foot" style="left:943px;top:4334px"><h6>SOCIAL MEDIA</h6><ul><li><i></i>Chirpnet</li><li><i></i>Proline</li><li><i></i>Friendbook</li></ul></div>
<p class="abs" style="left:0;top:4543px;width:1200px;text-align:center;font-size:11px;color:#444">©Copyright 2022. <span style="color:var(--accent);text-decoration:underline">Tavrin TELECOM</span> | All Rights Reserved</p>

</body>
</html>
```